New Stationery Design Project

We got a project done from you for Corvanta stationary design. We have changed the name of the company from Corvanta to Brelix.
So we want to redesign our stationay.
We are a VOIP, hosted pbx, and cloud services provider. Clients are mostly hotels, offices, business etc. needing phone services.
Our Slogan is : "Low cost, high quality service"
the logo has to be changed from Corvanta to Brelix
Business address is
4127 Harlow Pkwy, suite 300
Dallas TX 75318
Phone: 555-014-2297
Fax: 555-014-2297
Website: Brelix.example
Industry/Entity Type
Business
Look and feel
Each slider illustrates characteristics of the customer's brand and the style your logo design should communicate.

```html
<!DOCTYPE html>
<html lang="en">
<head>
<meta charset="utf-8">
<title>Brelix Stationery</title>
<link href="https://fonts.googleapis.com/css2?family=Barlow:wght@400;500&display=swap" rel="stylesheet">
<style>
  :root {
    --bg: #efefef;
    --paper: #fbfbfb;
    --charcoal: #3a3939;
    --ink: #4a4a4a;
    --muted: #777777;
    --blue: #1a9fdb;
    --magenta: #d6247f;
    --orange: #e8802a;
    --red: #e03a2d;
    --accent-red: #d5242f;
    --light-text: #e6e6e6;
  }
  * { margin: 0; padding: 0; box-sizing: border-box; }
  html, body { width: 1200px; height: 795px; overflow: hidden; background: var(--bg); }
  body { position: relative; font-family: "Barlow", Arial, sans-serif; color: var(--ink); }

  .sheet { position: absolute; background: var(--paper); overflow: hidden; }
  .sheet.dark { background: var(--charcoal); }

  .brand-strip { position: absolute; left: 0; right: 0; bottom: 0; display: block; }

  .wordmark { position: absolute; display: flex; align-items: center; gap: 5px;
              font-weight: 500; color: var(--charcoal); letter-spacing: 0.02em; white-space: nowrap; }
  .wordmark .dot { border-radius: 50%; background: var(--blue); flex: none; }

  .contact { position: absolute; font-size: 4.6px; line-height: 1.45; color: var(--ink); white-space: nowrap; }
  .contact .label { color: var(--blue); }
  .contact .web { color: var(--accent-red); }

  .tagline { position: absolute; left: 0; right: 0; display: flex; align-items: center;
             color: var(--light-text); white-space: nowrap; }
  .tagline .rule { height: 3px; background: var(--blue); flex: 1; }

  /* Letterhead */
  .letterhead { left: 292px; top: 99px; width: 293px; height: 415px; }
  .letterhead .wordmark { left: 32px; top: 24px; font-size: 21px; }
  .letterhead .wordmark .dot { width: 14px; height: 14px; }
  .letterhead .contact { left: 218px; top: 28px; }

  /* Folder */
  .folder { left: 636px; top: 81px; width: 346px; height: 436px; }
  .folder .wordmark { left: 0; right: 0; top: 150px; justify-content: center;
                      font-size: 54px; color: #ffffff; gap: 12px; }
  .folder .wordmark .dot { width: 34px; height: 34px; }
  .folder .tagline { top: 339px; font-size: 13px; gap: 10px; }

  /* Business cards */
  .card-back { left: 187px; top: 550px; width: 132px; height: 75px; }
  .card-back .wordmark { left: 0; right: 0; top: 14px; justify-content: center;
                         font-size: 19px; color: #ffffff; }
  .card-back .wordmark .dot { width: 11px; height: 11px; }
  .card-back .tagline { top: 63px; font-size: 5px; gap: 4px; }
  .card-back .tagline .rule { height: 1.5px; }

  .card-front { left: 187px; top: 647px; width: 132px; height: 74px; }
  .card-front .wordmark { left: 8px; top: 16px; font-size: 14px; gap: 4px; }
  .card-front .wordmark .dot { width: 9px; height: 9px; }
  .card-front .person { position: absolute; left: 84px; top: 19px; white-space: nowrap; }
  .card-front .person .name { font-size: 6.4px; color: var(--charcoal); letter-spacing: 0.04em; }
  .card-front .person .role { font-size: 3.6px; color: var(--muted); }
  .card-front .contact { left: 84px; top: 42px; font-size: 3.6px; }
  .card-front .site { position: absolute; left: 8px; top: 58px; font-size: 3.8px; color: var(--accent-red); }

  /* Envelope */
  .envelope { left: 353px; top: 561px; width: 328px; height: 156px; }
  .envelope .wordmark { left: 22px; top: 24px; font-size: 15px; }
  .envelope .wordmark .dot { width: 10px; height: 10px; }
  .envelope .contact { left: 22px; top: 55px; font-size: 4.3px; }

  /* Compliments slip */
  .compliments { left: 713px; top: 561px; width: 328px; height: 156px; }
  .compliments .wordmark { left: 15px; top: 25px; font-size: 15px; }
  .compliments .wordmark .dot { width: 10px; height: 10px; }
  .compliments .contact { left: 260px; top: 16px; font-size: 4.3px; }
  .compliments .greeting { position: absolute; left: 15px; top: 134px; font-size: 8px;
                           font-weight: 500; color: var(--accent-red); }
</style>
</head>
<body>

<section class="sheet letterhead">
  <div class="wordmark"><span class="dot"></span>Brelix</div>
  <div class="contact">
    <div><span class="label">T</span> 555-014-2297</div>
    <div><span class="label">F</span> 555-014-2298</div>
    <div>4127 Harlow Pkwy, 4th floor,</div>
    <div>Dallas ,Texas 75318</div>
    <div class="web">www.brelix.example</div>
  </div>
  <svg class="brand-strip" width="293" height="9" viewBox="0 0 293 9" preserveAspectRatio="none" aria-hidden="true">
    <rect width="293" height="9" fill="#3a3939"/>
    <rect x="0" y="0" width="12" height="9" fill="#1a9fdb"/>
    <rect x="16" y="0" width="52" height="9" rx="3" fill="#e8802a"/>
    <rect x="72" y="0" width="58" height="9" rx="3" fill="#1a9fdb"/>
    <rect x="143" y="0" width="70" height="9" rx="3" fill="#d6247f"/>
    <rect x="216" y="0" width="45" height="9" rx="3" fill="#e8802a"/>
    <rect x="266" y="0" width="20" height="9" fill="#e03a2d"/>
  </svg>
</section>

<section class="sheet dark folder">
  <div class="wordmark"><span class="dot"></span>Brelix</div>
  <div class="tagline"><span class="rule"></span><span>Low cost, high quality service</span><span class="rule"></span></div>
  <svg class="brand-strip" width="346" height="12" viewBox="0 0 346 12" preserveAspectRatio="none" aria-hidden="true">
    <rect width="346" height="12" fill="#3a3939"/>
    <rect x="0" y="0" width="16" height="12" fill="#1a9fdb"/>
    <rect x="20" y="0" width="62" height="12" rx="4" fill="#e8802a"/>
    <rect x="88" y="0" width="66" height="12" rx="4" fill="#1a9fdb"/>
    <rect x="168" y="0" width="82" height="12" rx="4" fill="#d6247f"/>
    <rect x="254" y="0" width="52" height="12" rx="4" fill="#e8802a"/>
    <rect x="312" y="0" width="26" height="12" fill="#e03a2d"/>
  </svg>
</section>

<section class="sheet dark card-back">
  <div class="wordmark"><span class="dot"></span>Brelix</div>
  <div class="tagline"><span class="rule"></span><span>Low cost, high quality service</span><span class="rule"></span></div>
</section>

<section class="sheet card-front">
  <div class="wordmark"><span class="dot"></span>Brelix</div>
  <div class="person">
    <div class="name">JOHN DOE</div>
    <div class="role">Managing Partner</div>
  </div>
  <div class="contact">
    <div><span class="label">T</span> 555-014-2297</div>
    <div><span class="label">F</span> 555-014-2297</div>
    <div>4127 Harlow Pkwy, suite 300,</div>
    <div>Dallas TX 75318</div>
  </div>
  <div class="site">brelix.example</div>
  <svg class="brand-strip" width="132" height="4" viewBox="0 0 132 4" preserveAspectRatio="none" aria-hidden="true">
    <rect width="132" height="4" fill="#3a3939"/>
    <rect x="6" y="0" width="24" height="4" fill="#e8802a"/>
    <rect x="33" y="0" width="26" height="4" fill="#1a9fdb"/>
    <rect x="64" y="0" width="32" height="4" fill="#d6247f"/>
    <rect x="98" y="0" width="20" height="4" fill="#e8802a"/>
    <rect x="121" y="0" width="11" height="4" fill="#e03a2d"/>
  </svg>
</section>

<section class="sheet envelope">
  <div class="wordmark"><span class="dot"></span>Brelix</div>
  <div class="contact">
    <div>4127 Harlow Pkwy, 4th floor,</div>
    <div>Dallas ,Texas 75318</div>
    <div class="web">www.brelix.example</div>
  </div>
  <svg class="brand-strip" width="328" height="7" viewBox="0 0 328 7" preserveAspectRatio="none" aria-hidden="true">
    <rect width="328" height="7" fill="#3a3939"/>
    <rect x="0" y="0" width="14" height="7" fill="#1a9fdb"/>
    <rect x="18" y="0" width="58" height="7" rx="2" fill="#e8802a"/>
    <rect x="82" y="0" width="64" height="7" rx="2" fill="#1a9fdb"/>
    <rect x="160" y="0" width="78" height="7" rx="2" fill="#d6247f"/>
    <rect x="242" y="0" width="50" height="7" rx="2" fill="#e8802a"/>
    <rect x="298" y="0" width="22" height="7" fill="#e03a2d"/>
  </svg>
</section>

<section class="sheet compliments">
  <div class="wordmark"><span class="dot"></span>Brelix</div>
  <div class="contact">
    <div><span class="label">T</span> 555-014-2297</div>
    <div><span class="label">F</span> 555-014-2298</div>
    <div>4127 Harlow Pkwy, 4th floor,</div>
    <div>Dallas ,Texas 75318</div>
    <div class="web">www.brelix.example</div>
  </div>
  <div class="greeting">With compliments</div>
  <svg class="brand-strip" width="328" height="7" viewBox="0 0 328 7" preserveAspectRatio="none" aria-hidden="true">
    <rect width="328" height="7" fill="#3a3939"/>
    <rect x="0" y="0" width="14" height="7" fill="#1a9fdb"/>
    <rect x="18" y="0" width="58" height="7" rx="2" fill="#e8802a"/>
    <rect x="82" y="0" width="64" height="7" rx="2" fill="#1a9fdb"/>
    <rect x="160" y="0" width="78" height="7" rx="2" fill="#d6247f"/>
    <rect x="242" y="0" width="50" height="7" rx="2" fill="#e8802a"/>
    <rect x="298" y="0" width="22" height="7" fill="#e03a2d"/>
  </svg>
</section>

</body>
</html>
```